Brindle painting & waterproofing business card.

Business cards updated to reflect photos attached. we have given the photos of the old business cards and some of our updated designs for other items we have here in the office. Please see attached. if anyone needs to contact us directly for clarification you can email us at brindlerestoration@mailvane.com

Industry/Entity Type

Construction

Contact Information for Business Card

See attached photos

Font styles to use
Other font styles liked:
• Same as photos

Colors
ec1f27

Requirements
Must have
• Employee Names,
• Gordon Brindle II, Supervisor/Owner
• Gord Brindle, President/Owner
• Tim Harker, Sales Representative
• Lou Marsten, Supervisor
• Change 20 years to 25
Nice to have
• ideas reflecting the attached photos
Should not have
• should not be exactly like attached photos as those are old business card but reflect to match new logo listed as kelvar van and cup photo.

```html
<!DOCTYPE html>
<html lang="en">
<head>
<meta charset="UTF-8">
<title>Brindle's Painting & Restoration – Business Card</title>
<link rel="stylesheet" href="https://fonts.googleapis.com/css2?family=Open+Sans:wght@400;600;700;800&family=Tinos:wght@400;700&display=swap">
<style>
  :root {
    --brand-red: #ec1f27;
    --deep-red: #b8141b;
    --swoosh-grey: #c9c9cb;
    --soft-grey: #ececee;
    --text-grey: #6b6b70;
    --ink: #1e1e22;
    --paper: #ffffff;
    --backdrop: #2b2e33;
  }
  * { box-sizing: border-box; margin: 0; padding: 0; }
  html, body { width: 1200px; height: 900px; overflow: hidden; }
  body {
    background: var(--backdrop);
    font-family: "Open Sans", Arial, sans-serif;
    display: flex;
    flex-direction: column;
    align-items: center;
    justify-content: center;
    gap: 56px;
  }
  .card {
    position: relative;
    width: 640px;
    height: 370px;
    border-radius: 22px;
    overflow: hidden;
    background: var(--paper);
  }
  .card-shapes { position: absolute; inset: 0; }

  /* Contact side */
  .staff {
    position: absolute;
    left: 30px;
    top: 120px;
    color: var(--paper);
    line-height: 1.35;
  }
  .staff-name { font-weight: 700; font-size: 24px; letter-spacing: -0.2px; }
  .staff-role { font-size: 14px; opacity: 0.85; }
  .staff-detail { font-size: 14px; font-weight: 600; }

  .wordmark {
    color: var(--brand-red);
    font-family: "Open Sans", Arial, sans-serif;
    font-weight: 800;
    text-transform: uppercase;
    line-height: 1;
    text-align: center;
  }
  .contact-side .wordmark {
    position: absolute;
    left: 300px;
    top: 40px;
    width: 260px;
  }
  .contact-side .wordmark-main { font-size: 42px; letter-spacing: 1px; }
  .contact-side .wordmark-sub { font-size: 15.5px; letter-spacing: 1.5px; margin-top: 6px; }
  .contact-side .rule {
    position: absolute; left: 312px; top: 124px; width: 236px; height: 2px;
    background: var(--brand-red);
  }
  .contact-list {
    position: absolute;
    left: 300px;
    top: 150px;
    list-style: none;
    font-family: "Tinos", "Times New Roman", serif;
    font-size: 17px;
    line-height: 1.3;
  }
  .contact-list li { display: flex; align-items: flex-start; gap: 8px; margin-bottom: 3px; }
  .contact-list svg { flex: none; margin-top: 3px; }
  .contact-list .address { color: var(--brand-red); font-weight: 700; }
  .contact-list .phone { font-weight: 700; color: var(--ink); }
  .contact-list .web { color: var(--ink); }

  /* Logo side */
  .logo-side .wordmark {
    position: absolute;
    left: 0; right: 0;
    top: 40px;
  }
  .logo-side .wordmark-main { font-size: 60px; letter-spacing: 2px; }
  .logo-side .wordmark-sub { font-size: 22px; letter-spacing: 2px; margin-top: 8px; }
  .tagline {
    position: absolute; left: 0; right: 0; top: 142px;
    text-align: center;
    font-family: "Tinos", "Times New Roman", serif;
    font-size: 17px;
    color: var(--ink);
  }
  .emblem {
    position: absolute; left: 270px; top: 172px;
    width: 100px; height: 52px;
  }
  .specialty {
    position: absolute; left: 0; right: 0; top: 236px;
    display: flex; align-items: center; justify-content: center; gap: 12px;
    color: var(--brand-red);
    font-weight: 700;
    font-size: 15px;
    text-transform: uppercase;
  }
  .specialty::before, .specialty::after {
    content: ""; width: 54px; height: 2px; background: var(--brand-red);
  }
  .services {
    position: absolute; left: 0; right: 0; top: 270px;
    text-align: center;
    color: var(--text-grey);
    font-size: 12.5px;
    text-transform: uppercase;
    line-height: 1.7;
    letter-spacing: 0.3px;
  }
</style>
</head>
<body>

  <section class="card contact-side" aria-label="Business card contact side">
    <svg class="card-shapes" width="640" height="370" viewBox="0 0 640 370">
      <defs>
        <linearGradient id="redBand" x1="0" y1="0" x2="1" y2="1">
          <stop offset="0" stop-color="#ec1f27"/>
          <stop offset="1" stop-color="#b8141b"/>
        </linearGradient>
        <linearGradient id="paperTone" x1="0" y1="0" x2="0" y2="1">
          <stop offset="0" stop-color="#f3f3f5"/>
          <stop offset="1" stop-color="#ffffff"/>
        </linearGradient>
      </defs>
      <rect width="640" height="370" fill="url(#paperTone)"/>
      <path d="M0,0 H300 C236,110 238,250 310,370 H0 Z" fill="#c9c9cb"/>
      <path d="M0,0 H262 C196,110 200,250 272,370 H0 Z" fill="url(#redBand)"/>
      <path d="M640,170 C575,230 520,300 480,370 H640 Z" fill="#c9c9cb"/>
      <path d="M640,196 C586,250 540,312 512,370 H640 Z" fill="url(#redBand)"/>
    </svg>

    <div class="staff">
      <p class="staff-name">Gordon Brindle II</p>
      <p class="staff-role">Supervisor / Owner</p>
      <p class="staff-detail">General Contractor</p>
      <p class="staff-detail">CGC1498620</p>
      <p class="staff-detail">Licensed &amp; Insured</p>
    </div>

    <div class="wordmark">
      <p class="wordmark-main">Brindle's</p>
      <p class="wordmark-sub">Painting &amp; Restoration</p>
    </div>
    <div class="rule"></div>

    <ul class="contact-list">
      <li class="address">
        <svg width="14" height="14" viewBox="0 0 14 14"><circle cx="7" cy="7" r="7" fill="#ec1f27"/><path d="M7 3.2a2.4 2.4 0 0 0-2.4 2.4C4.6 7.4 7 10.6 7 10.6s2.4-3.2 2.4-5A2.4 2.4 0 0 0 7 3.2z" fill="#fff"/><circle cx="7" cy="5.6" r="0.9" fill="#ec1f27"/></svg>
        <span>2470 NE 14th Ct Harbor Point FL 33071</span>
      </li>
      <li class="phone">
        <svg width="14" height="14" viewBox="0 0 14 14"><circle cx="7" cy="7" r="7" fill="#ec1f27"/><path d="M3.5 7.2 7 4l3.5 3.2V10.5h-2.2V8.4H5.7v2.1H3.5z" fill="#fff"/></svg>
        <span>954-310-4826</span>
      </li>
      <li class="phone">
        <svg width="14" height="14" viewBox="0 0 14 14"><circle cx="7" cy="7" r="7" fill="#ec1f27"/><path d="M4.6 3.6c.5-.3 1 0 1.2.5l.4 1c.1.4 0 .7-.3.9l-.4.3c.4.9 1.1 1.6 2 2l.3-.4c.2-.3.5-.4.9-.3l1 .4c.5.2.8.7.5 1.2-.4.8-1.2 1.1-2 .8C6.1 9.4 4.6 7.9 3.9 5.8c-.3-.9 0-1.7.7-2.2z" fill="#fff"/></svg>
        <span>954-310-9173</span>
      </li>
      <li class="web">
        <svg width="14" height="14" viewBox="0 0 14 14"><circle cx="7" cy="7" r="7" fill="#ec1f27"/><rect x="3.5" y="4.6" width="7" height="5" rx="0.6" fill="#fff"/><path d="M3.7 4.9 7 7.4l3.3-2.5" fill="none" stroke="#ec1f27" stroke-width="0.8"/></svg>
        <span>brindlerestoration@mailvane.com</span>
      </li>
      <li class="web">
        <svg width="14" height="14" viewBox="0 0 14 14"><circle cx="7" cy="7" r="7" fill="#ec1f27"/><circle cx="7" cy="7" r="3.6" fill="none" stroke="#fff" stroke-width="0.9"/><path d="M3.4 7h7.2M7 3.4c-1.5 2.2-1.5 5 0 7.2M7 3.4c1.5 2.2 1.5 5 0 7.2" fill="none" stroke="#fff" stroke-width="0.8"/></svg>
        <span>www.brindlerestoration.com</span>
      </li>
    </ul>
  </section>

  <section class="card logo-side" aria-label="Business card logo side">
    <svg class="card-shapes" width="640" height="370" viewBox="0 0 640 370">
      <defs>
        <linearGradient id="logoPaper" x1="0" y1="0" x2="1" y2="1">
          <stop offset="0" stop-color="#ffffff"/>
          <stop offset="0.5" stop-color="#efeff1"/>
          <stop offset="1" stop-color="#ffffff"/>
        </linearGradient>
      </defs>
      <rect width="640" height="370" fill="url(#logoPaper)"/>
      <path d="M60,255 C240,215 420,225 600,300" fill="none" stroke="#f6d5d6" stroke-width="10" opacity="0.6"/>
      <line x1="150" y1="132" x2="490" y2="132" stroke="#ec1f27" stroke-width="1.5"/>
    </svg>

    <div class="wordmark">
      <p class="wordmark-main">Brindle's</p>
      <p class="wordmark-sub">Painting &amp; Restoration</p>
    </div>
    <p class="tagline">Family Owned &amp; Operated</p>
    <svg class="emblem" role="img" aria-label="25 years in business emblem" viewBox="0 0 100 52">
      <rect width="100" height="52" rx="6" fill="#e4e4e7"/>
    </svg>
    <p class="specialty">Specializing in Hi-Rises &amp; Commercial</p>
    <p class="services">
      Concrete Restoration | Waterproofing | Painting | Expansion Joints<br>
      Caulking | Deck Coatings | Balustrades &amp; Railings
    </p>
  </section>

</body>
</html>
```